Business Cards for Internet Security Company

Awesome designers! This is the opportunity to help design cards for a forward thinking network security company. They use threat information gathered from peer groups to make intelligent decisions on what threats are relevant and which arent. ( not that you need this to do designs, but just so you know where they are coming from. ) :-)

We'd like to see a two side design and the deliverables will be in illustrator 4. The logo is attached and the logo colors are attached in the JPG and I've attached a an eps of the logo and icon

```html
<!DOCTYPE html>
<html lang="en">
<head>
<meta charset="utf-8">
<title>Halvane Business Cards</title>
<link rel="stylesheet" href="https://fonts.googleapis.com/css2?family=Questrial&family=Roboto+Condensed:wght@400;700&display=swap">
<style>
  :root {
    --backdrop: #ece9e4;
    --card: #ffffff;
    --navy: #1f3f6e;
    --steel: #3e6a94;
    --sky: #4a7fb8;
    --ink: #24456f;
  }
  html, body {
    margin: 0;
    padding: 0;
    width: 1200px;
    height: 913px;
    overflow: hidden;
    background: var(--backdrop);
  }
  .canvas {
    position: relative;
    width: 1200px;
    height: 913px;
  }
  .card {
    position: absolute;
    top: 308px;
    width: 520px;
    height: 297px;
    background: var(--card);
    box-shadow: 0 6px 18px rgba(0,0,0,0.16);
    overflow: hidden;
  }
  .card--front { left: 50px; }
  .card--back { left: 630px; }

  .brand {
    position: absolute;
    display: flex;
    align-items: center;
    gap: 10px;
    font-family: "Questrial", sans-serif;
    color: var(--steel);
  }
  .brand__dot {
    border-radius: 50%;
    background: var(--steel);
    flex: none;
  }
  .card--front .brand {
    left: 68px; top: 96px;
  }
  .card--front .brand__dot { width: 46px; height: 46px; }
  .card--front .brand__name {
    font-size: 84px;
    line-height: 1;
    letter-spacing: -1px;
  }
  .tagline {
    position: absolute;
    left: 126px; top: 190px;
    margin: 0;
    font-family: "Questrial", sans-serif;
    font-size: 22px;
    color: var(--sky);
    letter-spacing: 0.3px;
  }

  .card--back .brand {
    right: 24px; top: 24px;
    transform: rotate(180deg);
  }
  .card--back .brand__dot { width: 26px; height: 26px; }
  .card--back .brand__name { font-size: 46px; line-height: 1; }

  .contact {
    position: absolute;
    left: 28px; top: 64px;
    font-family: "Roboto Condensed", sans-serif;
  }
  .contact__name {
    margin: 0;
    font-size: 19px;
    font-weight: 700;
    color: var(--navy);
  }
  .contact__title {
    margin: 2px 0 22px;
    font-size: 14px;
    font-weight: 700;
    color: var(--sky);
  }
  .contact__list {
    list-style: none;
    margin: 0;
    padding: 0;
  }
  .contact__item {
    display: flex;
    align-items: flex-start;
    gap: 10px;
    margin-bottom: 5px;
    font-size: 14px;
    font-weight: 700;
    line-height: 1.25;
    color: var(--navy);
  }
  .contact__item svg {
    flex: none;
    width: 14px; height: 14px;
    margin-top: 1px;
    fill: var(--navy);
  }
  .band {
    position: absolute;
    left: 0; bottom: 0;
    width: 520px; height: 297px;
  }
</style>
</head>
<body>
<main class="canvas">

  <section class="card card--front" aria-label="Card front">
    <div class="brand">
      <span class="brand__dot"></span>
      <span class="brand__name">Halvane</span>
    </div>
    <p class="tagline">Shared Threat Insight</p>
  </section>

  <section class="card card--back" aria-label="Card back">
    <svg class="band" viewBox="0 0 520 297" aria-hidden="true">
      <defs>
        <linearGradient id="bandFill" x1="0" y1="1" x2="1" y2="0">
          <stop offset="0" stop-color="#1c3b68"/>
          <stop offset="1" stop-color="#45729c"/>
        </linearGradient>
      </defs>
      <path d="M0,297 L0,288 C180,284 360,238 520,140 L520,297 Z" fill="#c9d7e6"/>
      <path d="M0,297 L0,292 C190,290 370,248 520,156 L520,297 Z" fill="url(#bandFill)"/>
    </svg>
    <div class="brand">
      <span class="brand__dot"></span>
      <span class="brand__name">Halvane</span>
    </div>

    <div class="contact">
      <h2 class="contact__name">Mark Tollin</h2>
      <p class="contact__title">Chief Executive Officer &amp; Co-Founder</p>
      <ul class="contact__list">
        <li class="contact__item">
          <svg viewBox="0 0 24 24"><path d="M12 2a7 7 0 0 0-7 7c0 5 7 13 7 13s7-8 7-13a7 7 0 0 0-7-7zm0 9.5A2.5 2.5 0 1 1 12 6.5a2.5 2.5 0 0 1 0 5z"/></svg>
          <span>Your Communication Address in<br>just two line</span>
        </li>
        <li class="contact__item">
          <svg viewBox="0 0 24 24"><path d="M6.6 10.8a15 15 0 0 0 6.6 6.6l2.2-2.2a1 1 0 0 1 1-.25 11.4 11.4 0 0 0 3.6.57 1 1 0 0 1 1 1V20a1 1 0 0 1-1 1A17 17 0 0 1 3 4a1 1 0 0 1 1-1h3.5a1 1 0 0 1 1 1c0 1.25.2 2.45.57 3.6a1 1 0 0 1-.25 1z"/></svg>
          <span>(000) 000-000-000</span>
        </li>
        <li class="contact__item">
          <svg viewBox="0 0 24 24"><path d="M2 5h20v14H2z M2 5l10 8 10-8" fill="none" stroke="#1f3f6e" stroke-width="2.4"/></svg>
          <span>yourname@yourwebsite.com</span>
        </li>
        <li class="contact__item">
          <svg viewBox="0 0 24 24"><circle cx="12" cy="12" r="9" fill="none" stroke="#1f3f6e" stroke-width="2"/><path d="M3 12h18M12 3c3 3 3 15 0 18M12 3c-3 3-3 15 0 18" fill="none" stroke="#1f3f6e" stroke-width="1.6"/></svg>
          <span>www.yourwebsite.com</span>
        </li>
      </ul>
    </div>
  </section>

</main>
</body>
</html>
```